NEED Homepage Website Design for Event Planning Business

We need a homepage mockup for an event planning company based in Massachusetts. We provide a custom trailer to rent along with chairs, tables, lighting, etc.

Please add a "Check Availability" call to action which is just a form
- First & Last Name
- Phone
- Email Address
- Date Request

Add an Instagram section (use attached photos as we do not even have an IG account yet)

1 page

```html
<!DOCTYPE html>
<html lang="en">
<head>
<meta charset="utf-8">
<title>Northfield Entertainment – Event Trailer Rentals</title>
<link href="https://fonts.googleapis.com/css2?family=Roboto:wght@300;400;500;700;900&display=swap" rel="stylesheet">
<style>
:root{
  --red:#c4151c;
  --ink:#111;
  --text:#555;
  --grey-bg:#f3f3f3;
  --dark:#0b0b0b;
  --white:#fff;
  --photo-green:#4a5a3c;
  --photo-grey:#7f8687;
}
*{box-sizing:border-box;margin:0;padding:0}
html,body{width:1200px;height:3658px;overflow:hidden}
body{font-family:'Roboto',sans-serif;color:var(--ink);background:var(--white);position:relative}
.abs{position:absolute}
.btn{position:absolute;background:var(--red);color:var(--white);font-weight:700;font-size:15px;display:flex;align-items:center;justify-content:center;text-transform:uppercase;letter-spacing:.2px}
.bar{position:absolute;left:578px;width:44px;height:3px;background:var(--red)}
.center{position:absolute;left:0;width:1200px;text-align:center}

/* header */
.site-header{position:absolute;top:0;left:0;width:1200px;height:88px;border-top:3px solid var(--red);background:var(--white)}
.brand{position:absolute;left:145px;top:24px;font-size:22px;font-weight:700;display:flex;align-items:center;gap:8px}
.brand-mark{width:14px;height:14px;background:var(--ink)}
.nav{position:absolute;right:145px;top:30px;display:flex;gap:28px;font-size:15px;font-weight:500}
.nav a{color:var(--ink);text-decoration:none;padding-bottom:8px}
.nav a.active{border-bottom:2px solid var(--red)}

/* hero */
.hero{position:absolute;top:88px;left:0;width:1200px;height:584px;background:linear-gradient(180deg,#3d4438 0%,#50584a 45%,#2b2f28 100%)}
.hero-title{top:188px;font-size:80px;font-weight:900;color:var(--white);letter-spacing:-1px;text-shadow:0 3px 6px rgba(0,0,0,.5)}
.hero-sub{top:292px;font-size:28px;font-weight:700;color:var(--white);line-height:32px;text-shadow:0 2px 4px rgba(0,0,0,.6)}
.dots{position:absolute;top:532px;left:568px;display:flex;gap:6px}
.dots span{width:8px;height:8px;border-radius:50%;background:var(--white)}
.dots span.on{background:var(--red)}

/* availability */
.avail{position:absolute;top:672px;left:0;width:1200px;height:171px;background:rgba(0,0,0,.92)}
.avail h2{top:30px;font-size:31px;font-weight:700;color:var(--white)}
.field{position:absolute;top:100px;width:155px;height:36px;border:1px solid #ddd;color:var(--white);font-size:11px;padding:12px 18px}

/* text blocks */
.para{font-size:14px;line-height:26.5px;color:var(--text);font-weight:300}
.sec-title{font-size:48px;font-weight:300;color:var(--ink)}
.sec-title b{font-weight:900}

/* services */
.services{position:absolute;top:1392px;left:0;width:1200px;height:383px;background:var(--grey-bg)}
.tile{position:absolute;width:300px;height:275px}
.tile-text{padding:32px 42px}
.tile-text h3{font-size:20px;font-weight:500;line-height:26px;margin-bottom:16px}
.tile-text p{font-size:12.5px;line-height:22.5px;color:var(--text);font-weight:300}
.tile-text .btn{position:static;width:124px;height:38px;font-size:14px;margin-top:18px}

/* faq */
.faq-card{position:absolute;left:537px;top:2627px;width:518px;height:373px;background:var(--white)}
.faq-card h4{position:absolute;left:47px;top:78px;font-size:20px;font-weight:500;color:var(--red);line-height:30px}
.faq-card p{position:absolute;left:47px;top:152px;width:460px;font-size:12.5px;line-height:22.5px;color:var(--text);font-weight:300}

/* insta strip */
.insta{position:absolute;top:3137px;height:273px;width:296px}
.arrow{position:absolute;top:3255px;width:40px;height:54px;background:var(--dark);display:flex;align-items:center;justify-content:center}

/* footer */
.footer{position:absolute;top:3410px;left:0;width:1200px;height:248px;background:var(--dark);color:var(--white)}
.footer h5{position:absolute;left:145px;top:58px;font-size:19px;font-weight:500}
.footer h5 span{color:var(--red)}
.footer .lead{position:absolute;left:145px;top:96px;font-size:13.5px;font-weight:300}
.email{position:absolute;left:483px;top:65px;width:421px;height:46px;border:1px solid #333;font-size:11px;padding:16px 18px}
.socials{position:absolute;left:145px;top:200px;display:flex;gap:30px}
.socials span{width:24px;height:24px;border-radius:50%;background:var(--white)}
.legal{position:absolute;right:145px;top:206px;font-size:13px;font-weight:300}
</style>
</head>
<body>

<header class="site-header">
  <div class="brand"><span class="brand-mark"></span>Northfield Entertainment</div>
  <nav class="nav">
    <a class="active">Home</a><a>About</a><a>Services</a><a>Frequently Asked Questions</a><a>Contact</a>
  </nav>
</header>

<section class="hero" role="img" aria-label="Entertainment trailer with patio umbrellas, barrel tables and bar stools on a driveway"></section>
<div class="center hero-title">NFE ENTERTAINMENT</div>
<div class="center hero-sub">We provide a custom trailer to rent along with<br>chairs, tables, lighting,etc</div>
<div class="btn" style="left:510px;top:477px;width:180px;height:56px">Get Started</div>
<div class="dots"><span></span><span></span><span class="on"></span><span></span><span></span></div>

<section class="avail">
  <h2 class="center">Check Availability</h2>
  <div class="field" style="left:143px">First Name</div>
  <div class="field" style="left:308px">Last Name</div>
  <div class="field" style="left:473px">Phone</div>
  <div class="field" style="left:638px">Email Address</div>
  <div class="field" style="left:803px;display:flex;justify-content:space-between">Date Request
    <svg width="11" height="11" viewBox="0 0 11 11"><rect x="1" y="2" width="9" height="8" fill="none" stroke="#fff"/><rect x="1" y="2" width="9" height="2" fill="#fff"/></svg></div>
  <div class="btn" style="left:966px;top:100px;width:91px;height:36px">Submit</div>
</section>

<h2 class="center sec-title" style="top:932px"><b>WELCOME TO</b></h2>
<div class="center" style="top:992px;font-size:32px;font-weight:300">NORTHFIELD-ENTERTAINMENT</div>
<div class="bar" style="top:1051px"></div>
<p class="center para" style="top:1090px;padding:0 200px">We provide everything you need to host any event desired!! Our goal is to provide an atmosphere that will blow away the competition and leave you feeling that you hosted an event which will leave everyone talking!! We are event planners who will provide all the goods and bring new ideas to the table that have never been done before! Starting with our main attraction the NFE entertainment trailer which was just completed last summer! We typically start booking your event with the entertainment trailer and build off of that. Whatever the occasion and whatever you desire, we will go beyond your expectations!</p>
<div class="btn" style="left:517px;top:1261px;width:166px;height:48px;font-size:16px">Read More</div>

<section class="services">
  <h2 class="center sec-title" style="top:92px"><b>OUR</b> SERVICES</h2>
  <div class="bar" style="top:168px"></div>
  <p class="center para" style="top:208px;padding:0 200px">Full Entertainment Trailer Rental:For the price of $1135.00 we will deliver the trailer within 30 miles for no additional fee. That includes the Trailer to be setup and broken down on location and the use of the entire Bar area, storage room, and two Bathrooms. The bathrooms come fully stocked with all the necessary supplies needed for that particular event.<br>Additional pricing for adding equipment with the trailer package or to be rented separate below.</p>
</section>

<div class="tile tile-text" style="left:0;top:1775px">
  <h3>Lighting rental<br>and setup</h3>
  <p>We have classic restaurant style patio lights we hang inside and along the tent. We charge $25 for our setup fee and use of the lights for every 12 foot</p>
  <div class="btn">Read More</div>
</div>
<div class="tile" style="left:300px;top:1775px;background:linear-gradient(160deg,#2f3a28,#6b6e52)" role="img" aria-label="Patio umbrella over a wooden barrel table with stools"></div>
<div class="tile tile-text" style="left:600px;top:1775px">
  <h3>DJs, Bartenders<br>and Party hosts.</h3>
  <p>DJs are typically subcontracted but we have two DJs who work for Northfield-Entertainment as well. Most of our DJs cost about $140 an hour.</p>
  <div class="btn">Read More</div>
</div>
<div class="tile" style="left:900px;top:1775px;background:linear-gradient(160deg,#8d9290,#3d4a3a)" role="img" aria-label="Covered trailer porch with lanterns under a tent"></div>

<div class="tile" style="left:0;top:2050px;background:linear-gradient(160deg,#c9cccb,#5f6656)" role="img" aria-label="Tent interior with round tables and barrel table"></div>
<div class="tile tile-text" style="left:300px;top:2050px">
  <h3>Whiskey Barrel Rentals</h3>
  <p>Our stained Rustic Whiskey/wine barrels are $35 a piece and provide a nice touch to the rustic farmhouse style trailer. They also create an additional area to gather to rest your cocktails or maybe</p>
  <div class="btn">Read More</div>
</div>
<div class="tile" style="left:600px;top:2050px;background:linear-gradient(160deg,#d9dcdc,#556046)" role="img" aria-label="Trailer with attached white tent on a lawn"></div>
<div class="tile tile-text" style="left:900px;top:2050px">
  <h3>Tent Setup pricing</h3>
  <p>Tents which are connected to the side of the trailer are rented in 12 foot sections. Each section extends12 feet out from the side of the trailer and is 25 in length which is the same size as the trailer.</p>
  <div class="btn">Read More</div>
</div>

<h2 class="center sec-title" style="top:2425px"><b>FREQUENTLY</b> ASKED QUESTIONS</h2>
<div class="bar" style="top:2505px"></div>
<div class="abs" style="left:145px;top:2580px;width:460px;height:465px;background:linear-gradient(170deg,#d4d6d5,#6e7466 60%,#3b3a33)" role="img" aria-label="Tent with string lights, round tables and bar stools"></div>
<div class="faq-card">
  <h4>HOW DOES THE TRAILER HAVE LIGHTING<br>AND WATER?</h4>
  <p>During the setup process of the NFE entertainment trailer we will connect a black garden hose to the closest connection available and we will run a power cord connection from the trailer to a typical common 110 volt outlet. Most likely these will run across the driveway or an area your guests will be walking so we will include a plastic yellow safety protector for the cord and hose to run through making it safe for guests to walk over.</p>
</div>

<div class="insta" style="left:0;background:linear-gradient(160deg,#6a7a55,#a0826a)" role="img" aria-label="Trailer bar counter with stools"></div>
<div class="insta" style="left:300px;background:linear-gradient(160deg,#a3161b,#7e0e12)" role="img" aria-label="Trailer photo with red overlay">
  <svg class="abs" style="left:130px;top:118px" width="36" height="36" viewBox="0 0 36 36"><rect x="2" y="2" width="32" height="32" fill="none" stroke="#fff" stroke-width="3"/></svg>
</div>
<div class="insta" style="left:600px;background:linear-gradient(170deg,#a9adb0,#5b6c45)" role="img" aria-label="Trailer on a driveway in front of a house"></div>
<div class="insta" style="left:904px;background:linear-gradient(160deg,#4f6a3e,#c9c6bd)" role="img" aria-label="Trailer porch with lanterns and trees"></div>
<div class="arrow" style="left:0"><svg width="14" height="22" viewBox="0 0 14 22"><path d="M12 2 3 11l9 9" fill="none" stroke="#fff" stroke-width="3"/></svg></div>
<div class="arrow" style="left:1160px"><svg width="14" height="22" viewBox="0 0 14 22"><path d="M2 2l9 9-9 9" fill="none" stroke="#fff" stroke-width="3"/></svg></div>

<footer class="footer">
  <h5>SIGN UP <span>NEWSLETTER</span></h5>
  <div class="lead">Lorem ipsum dolor sit onsectetur adipiscing elit</div>
  <div class="email">Enter Email</div>
  <div class="btn" style="left:917px;top:65px;width:140px;height:46px;font-size:16px;font-weight:500">Subscribe</div>
  <div class="socials"><span></span><span></span><span></span><span></span></div>
  <div class="legal">© 2021 Northfield Entertainment. All rights reserved &nbsp;|&nbsp; Privacy &nbsp;|&nbsp; Terms of Use</div>
</footer>

</body>
</html>
```